Vendor Managed Inventory Talking points/Customer hand out

Looking for a single page flyer/Customer handout to be a sell sheet for our Vendor managed Inventory programs
Title: VMI benefits
Risk management:
Identification of Items and values that are sole sourced
Ongoing plans to reduce exposure to sole sourced items
Schedule planning to eliminate freight and outages
Reducing the hidden costs of forecasting errors
(Note; with us managing the point of use we can more accurately forecast)
Managing ever shortening of product lifecycles, minimizing obsolescence
Zero Inventory Exposure:
Minimized or Zero inventory on commodity items
Greatly reducing the Weighted Cost of Capital (WACC)
Reduced WACC can help in calculating Hurdle Rates
True point of use billing:
Allows for better tracking and allocation of expenses from a job-job basis
Custom labeling:
Including things like customer part numbers, exp dates, internal hazmat codes
Insures accurate processes with current materials
Helps to meet 5S requirements
Required for certain audits
Lot tracking/Shelf life:
Active assistance in managing Date Codes/Lot Tracking
Shortened shelf life products identified and managed
Plain statement of expiration dates on products. Calculations are not required
Taken as a whole we can help calculate TRUE management and landed costs of products. Focusing only on the price of items is like looking at just the exposed part of an iceberg. Let RQ7T help you to see what's underneath.
I have attached some other brochures and flyers for style reference
more info on our website too. www.rq7t-example.com
Target Market(s)
Electronics manufacturers
Industry/Entity Type
Electronics
Look and feel

```html
<!DOCTYPE html>
<html lang="en">
<head>
<meta charset="utf-8">
<title>RQ7T – VMI Benefits</title>
<link href="https://fonts.googleapis.com/css2?family=Montserrat:wght@400;500;700&display=swap" rel="stylesheet">
<style>
  :root{
    --page:#ffffff;
    --navy:rgba(28,22,108,0.92);
    --pill:#6fcadb;
    --teal-band:rgba(58,170,182,0.88);
    --wave:#5bb9c9;
    --brand-blue:#1d4f9e;
    --ink:#ffffff;
  }
  *{box-sizing:border-box;margin:0;padding:0}
  html,body{width:1200px;height:1200px;overflow:hidden;background:var(--page)}
  body{font-family:'Montserrat',sans-serif;position:relative}
  .flyer{position:absolute;left:224px;top:18px;width:752px;height:1165px;overflow:hidden;background:#d9d9d9}
  .flyer__photo{position:absolute;inset:0;
    background:radial-gradient(ellipse at 70% 75%,#3d3d40 0%,#7a7a7e 35%,#c9c9cb 70%,#e2e2e2 100%)}
  .flyer__header{position:absolute;left:0;top:0;width:752px;height:160px}
  .brand{position:absolute;right:70px;top:58px;display:flex;align-items:center;gap:10px;
    color:var(--brand-blue);font-weight:700;font-size:34px;letter-spacing:1px;line-height:1}
  .brand__mark{width:14px;height:14px;border-radius:50%;background:var(--brand-blue)}
  .panel{position:absolute;left:62px;width:616px;background:var(--navy);border-radius:14px;
    color:var(--ink);font-size:15px;line-height:18.4px;text-align:center;
    display:flex;flex-direction:column;justify-content:center;padding-top:18px}
  .pill{position:absolute;background:var(--pill);border-radius:30px;color:var(--ink);
    display:flex;align-items:center;justify-content:center;gap:10px;font-size:19px;font-weight:500;letter-spacing:.3px;z-index:2}
  .pill svg{width:40px;height:40px;flex:none}
  .closing{position:absolute;left:62px;top:1033px;width:616px;height:119px;background:var(--teal-band);
    border-radius:14px;color:var(--ink);font-size:15px;line-height:18.4px;text-align:center;
    display:flex;flex-direction:column;justify-content:center;padding:0 12px}
  .closing__url{font-weight:700}
</style>
</head>
<body>
<div class="flyer">
  <div class="flyer__photo" role="img" aria-label="Greyscale photo of an electronics workbench with a circuit board and test probes"></div>

  <svg class="flyer__header" viewBox="0 0 752 160" aria-hidden="true">
    <path d="M0 95 C90 35 220 15 330 65 C450 125 600 150 752 130 L752 0 L0 0 Z" fill="#ffffff"/>
    <path d="M0 95 C90 35 220 15 330 65 C450 125 600 150 752 130" fill="none" stroke="var(--wave)" stroke-width="6"/>
  </svg>
  <div class="brand">
    <span class="brand__mark"></span>
    <span class="brand__name">RQ7T</span>
  </div>

  <div class="pill" style="left:234px;top:146px;width:284px;height:58px">
    <svg viewBox="0 0 40 40"><path d="M20 5 L37 35 H3 Z" fill="none" stroke="#fff" stroke-width="3" stroke-linejoin="round"/><path d="M20 15 V26" stroke="#fff" stroke-width="3"/><circle cx="20" cy="30.5" r="1.8" fill="#fff"/></svg>
    RISK MANAGEMENT
  </div>
  <div class="panel" style="top:186px;height:164px">
    <p>Identification of Items and values that are sole sourced</p>
    <p>Ongoing plans to reduce exposure to sole sourced items</p>
    <p>Schedule planning to eliminate freight and outages</p>
    <p>Reducing the hidden costs of forecasting errors</p>
    <p>(Note; with us managing the point of use we can more accurately forecast)</p>
    <p>Managing ever shortening of product lifecycles, minimizing obsolescence</p>
  </div>

  <div class="pill" style="left:192px;top:368px;width:368px;height:58px">
    <svg viewBox="0 0 40 40"><rect x="7" y="6" width="26" height="31" rx="2" fill="none" stroke="#fff" stroke-width="2.5"/><rect x="14" y="3" width="12" height="6" rx="1" fill="#fff"/><path d="M12 16h2M17 16h11M12 22h2M17 22h11M12 28h2M17 28h11" stroke="#fff" stroke-width="2"/></svg>
    ZERO INVENTORY EXPOSURE
  </div>
  <div class="panel" style="top:407px;height:113px">
    <p>Minimized or Zero inventory on commodity items</p>
    <p>Greatly reducing the Weighted Cost of Capital (WACC)</p>
    <p>Reduced WACC can help in calculating Hurdle Rates</p>
  </div>

  <div class="pill" style="left:192px;top:538px;width:368px;height:58px">
    <svg viewBox="0 0 40 40"><path d="M6 3h24v26l-3 2-3-2-3 2-3-2-3 2-3-2-3 2-3-2Z" fill="#fff"/><path d="M10 10h16M10 15h16M10 20h10" stroke="var(--pill)" stroke-width="2"/><circle cx="30" cy="31" r="7" fill="#fff"/><path d="M26.5 31l2.5 2.5 4.5-4.5" fill="none" stroke="var(--pill)" stroke-width="2"/></svg>
    TRUE POINT OF USE BILLING
  </div>
  <div class="panel" style="top:577px;height:77px">
    <p>Allows for better tracking and allocation of expenses from a job-job basis</p>
  </div>

  <div class="pill" style="left:234px;top:670px;width:284px;height:59px">
    <svg viewBox="0 0 40 40"><path d="M4 22 L18 4 H30 V16 L14 34 Z" fill="#fff"/><circle cx="24" cy="10" r="2.5" fill="var(--pill)"/><path d="M31 24v12M25 30h12" stroke="#fff" stroke-width="4"/></svg>
    CUSTOM LABELING
  </div>
  <div class="panel" style="top:710px;height:132px">
    <p>Including things like customer part numbers, exp dates, internal hazmat codes</p>
    <p>Insures accurate processes with current materials</p>
    <p>Helps to meet 5S requirements</p>
    <p>Required for certain audits</p>
  </div>

  <div class="pill" style="left:202px;top:860px;width:348px;height:56px">
    <svg viewBox="0 0 40 40"><circle cx="20" cy="20" r="12" fill="none" stroke="#fff" stroke-width="3"/><circle cx="20" cy="20" r="3.5" fill="none" stroke="#fff" stroke-width="2.5"/><path d="M20 2v8M20 30v8M2 20h8M30 20h8" stroke="#fff" stroke-width="3"/></svg>
    LOT TRACKING/SHELF LIFE
  </div>
  <div class="panel" style="top:898px;height:118px">
    <p>Active assistance in managing Date Codes/Lot Tracking</p>
    <p>Shortened shelf life products identified and managed</p>
    <p>Plain statement of expiration dates on products. Calculations are not required</p>
  </div>

  <div class="closing">
    <p>Taken as a whole we can help calculate TRUE management and landed costs of products. Focusing only on the price of items is like looking at just the exposed part of an iceberg. Let RQ7T help you to see what's underneath.</p>
    <p class="closing__url">www.rq7t-example.com</p>
  </div>
</div>
</body>
</html>
```